The Council for Stewardship in Harbor Ventures Needs a Banner Design

We (C-SoHV) need a retractable banner design that will include our logo, graphics/collage that encompass the capital projects theme, our Forum and/or buildings (some sample pics are attached), and our mission.

Designer does not have to use specific pics that are attached - these are examples. However, they can use these if they'd like.

Target Market(s)

Builders, Contractors, Engineers, Architects, Developers, design professionals

Industry/Entity Type

Leadership

Colors
0355a3
3276b5
85abd2
cedeed
00a990
33b8a4
86cfc6
edf8f6

Requirements
Must have
• Logo, graphics/collage that encompass the capital projects theme, our Forum and/or buildings (some sample pics are attached), and our mission. Fit to 2.5'x6' Vertical Banner.
• Our Mission is To: Evolve the capital projects industry through sharing of knowledge for optimized leadership, delivery and performance.
Nice to have
• Designer does not have to use specific pics that are attached - these are examples. However, they can use these if they'd like.
Should not have
• Colors that clash with logo.

```html
<!DOCTYPE html>
<html lang="en">
<head>
<meta charset="utf-8">
<title>C-SoHV Retractable Banner Concepts</title>
<link href="https://fonts.googleapis.com/css2?family=Arimo:wght@400;700&display=swap" rel="stylesheet">
<style>
  :root {
    --lime: #a8cf3a;
    --navy: #27409b;
    --navy-deep: #1f3488;
    --ink: #2b3c93;
    --muted: #3b3f4a;
    --white: #ffffff;
    --label: #e3141b;
  }
  * { box-sizing: border-box; margin: 0; padding: 0; }
  html, body { width: 1200px; height: 960px; overflow: hidden; background: var(--white); }
  body { position: relative; font-family: "Arimo", Arial, sans-serif; }

  .banner {
    position: absolute; top: 64px; width: 304px; height: 708px;
    background: var(--white); overflow: hidden;
  }
  .banner--one { left: 51px; }
  .banner--two { left: 447px; }
  .banner--three { left: 843px; }

  .top-band { position: absolute; top: 0; left: 0; width: 304px; height: 56px; }

  .brand {
    position: absolute; top: 70px; left: 0; width: 304px; height: 80px;
    display: flex; align-items: center; gap: 14px; padding-left: 30px;
  }
  .brand-mark { width: 62px; height: 62px; border-radius: 50%; background: var(--navy); flex: none; }
  .brand-text { display: flex; flex-direction: column; }
  .brand-name { font-size: 34px; font-weight: 400; color: var(--muted); line-height: 1; letter-spacing: 0.5px; }
  .brand-rule { width: 156px; height: 1px; background: var(--muted); margin: 5px 0 4px; }
  .brand-full { font-size: 7.4px; color: var(--muted); white-space: nowrap; }

  .hero { position: absolute; top: 160px; left: 0; width: 304px; height: 204px; }
  .hero--one { background: linear-gradient(160deg, #55595f 0%, #7d8087 40%, #b7c2c9 60%, #3e4248 100%); }
  .hero--two { background: linear-gradient(180deg, #e8eef2 0%, #c9d6de 40%, #4e5d72 75%, #2d3648 100%); }
  .hero--three { background: linear-gradient(180deg, #8fa7b8 0%, #5f7688 40%, #3a4654 75%, #c5ccd2 100%); }
  .hero-arch { position: absolute; top: 0; left: 0; width: 304px; height: 14px; }

  .mission {
    position: absolute; top: 364px; left: 0; width: 304px; height: 94px;
    background: var(--lime); text-align: center; padding-top: 13px;
  }
  .mission-title { font-size: 20.5px; font-weight: 700; color: var(--ink); letter-spacing: 0.2px; }
  .mission-body { font-size: 13px; color: var(--muted); line-height: 14px; margin-top: 5px; }

  .pillars {
    position: absolute; top: 458px; left: 0; width: 304px; height: 96px;
    background: var(--navy); padding: 3px 0 0 38px;
  }
  .pillar { display: flex; align-items: center; height: 28.5px; gap: 12px; }
  .pillar svg { width: 24px; height: 22px; flex: none; }
  .pillar-name { color: var(--white); font-size: 21px; font-weight: 700; letter-spacing: 0.4px; }

  .skyline {
    position: absolute; top: 552px; left: 0; width: 304px; height: 156px;
    background: linear-gradient(170deg, #d7e6f2 0%, #8fb6dc 35%, #3e6aa8 70%, #1f3a6a 100%);
  }
  .skyline-edge { position: absolute; top: 552px; left: 0; width: 304px; height: 14px; }

  .concept-label {
    position: absolute; top: 870px; width: 304px; text-align: center;
    font-size: 46px; font-weight: 400; color: var(--label);
  }
  .concept-label--one { left: 51px; }
  .concept-label--two { left: 447px; }
  .concept-label--three { left: 843px; }
</style>
</head>
<body>

<svg width="0" height="0" style="position:absolute">
  <defs>
    <symbol id="icon-leadership" viewBox="0 0 24 22">
      <circle cx="12" cy="3" r="2.6" fill="#fff"/>
      <rect x="10" y="6" width="4" height="4" fill="#fff"/>
      <path d="M12 10v3M4 13h16M4 13v2M12 13v2M20 13v2" stroke="#fff" stroke-width="1.4" fill="none"/>
      <circle cx="4" cy="16.5" r="1.8" fill="#fff"/><rect x="2" y="18.5" width="4" height="3.5" fill="#fff"/>
      <circle cx="12" cy="16.5" r="1.8" fill="#fff"/><rect x="10" y="18.5" width="4" height="3.5" fill="#fff"/>
      <circle cx="20" cy="16.5" r="1.8" fill="#fff"/><rect x="18" y="18.5" width="4" height="3.5" fill="#fff"/>
    </symbol>
    <symbol id="icon-delivery" viewBox="0 0 24 22">
      <path d="M1 6h8v10H1zM9 9h4l3 4v3H9z" fill="none" stroke="#fff" stroke-width="1.6"/>
      <circle cx="4.5" cy="18" r="2.2" fill="#fff"/><circle cx="12.5" cy="18" r="2.2" fill="#fff"/>
      <rect x="17" y="6" width="6" height="10" fill="none" stroke="#fff" stroke-width="1.4"/>
      <path d="M17 6l6 10M23 6l-6 10" stroke="#fff" stroke-width="1"/>
    </symbol>
    <symbol id="icon-performance" viewBox="0 0 24 22">
      <rect x="2" y="15" width="3" height="7" fill="#fff"/>
      <rect x="7" y="12" width="3" height="10" fill="#fff"/>
      <rect x="12" y="9" width="3" height="13" fill="#fff"/>
      <rect x="17" y="6" width="3" height="16" fill="#fff"/>
      <path d="M2 12L16 3" stroke="#fff" stroke-width="1.8"/>
      <path d="M13 1.5l6-0.5-2.5 5.5z" fill="#fff"/>
    </symbol>
    <symbol id="top-band" viewBox="0 0 304 56">
      <rect width="304" height="56" fill="#fff"/>
      <path d="M0 0h304v44Q152 22 0 44z" fill="#a8cf3a"/>
      <path d="M0 44Q152 22 304 44v6Q152 28 0 50z" fill="#27409b"/>
    </symbol>
  </defs>
</svg>

<!-- Concept 1 -->
<section class="banner banner--one">
  <svg class="top-band" viewBox="0 0 304 56"><use href="#top-band"/></svg>
  <div class="brand">
    <span class="brand-mark"></span>
    <div class="brand-text">
      <span class="brand-name">C-SoHV</span>
      <span class="brand-rule"></span>
      <span class="brand-full">The Council for Stewardship in Harbor Ventures</span>
    </div>
  </div>
  <div class="hero hero--one" role="img" aria-label="Overhead photo of a project team meeting around a table with plans and a solar panel"></div>
  <svg class="hero-arch" style="top:160px" viewBox="0 0 304 14" preserveAspectRatio="none"><path d="M0 0h304v12Q152 -4 0 12z" fill="#fff"/></svg>
  <div class="mission">
    <h2 class="mission-title">OUR MISSION IS TO:</h2>
    <p class="mission-body">To evolve the capital projects industry<br>through sharing of knowledge for<br>optimized:</p>
  </div>
  <ul class="pillars">
    <li class="pillar"><svg><use href="#icon-leadership"/></svg><span class="pillar-name">LEADERSHIP</span></li>
    <li class="pillar"><svg><use href="#icon-delivery"/></svg><span class="pillar-name">DELIVERY</span></li>
    <li class="pillar"><svg><use href="#icon-performance"/></svg><span class="pillar-name">PERFORMANCE</span></li>
  </ul>
  <div class="skyline" role="img" aria-label="Photo of glass office towers under construction with cranes against a blue sky"></div>
  <svg class="skyline-edge" viewBox="0 0 304 14" preserveAspectRatio="none"><path d="M0 0h304v2Q152 16 0 2z" fill="#27409b"/></svg>
</section>

<!-- Concept 2 -->
<section class="banner banner--two">
  <svg class="top-band" viewBox="0 0 304 56"><use href="#top-band"/></svg>
  <div class="brand">
    <span class="brand-mark"></span>
    <div class="brand-text">
      <span class="brand-name">C-SoHV</span>
      <span class="brand-rule"></span>
      <span class="brand-full">The Council for Stewardship in Harbor Ventures</span>
    </div>
  </div>
  <div class="hero hero--two" role="img" aria-label="Photo of engineers and builders in hard hats meeting in a bright boardroom"></div>
  <svg class="hero-arch" style="top:160px" viewBox="0 0 304 14" preserveAspectRatio="none"><path d="M0 0h304v12Q152 -4 0 12z" fill="#fff"/></svg>
  <div class="mission">
    <h2 class="mission-title">OUR MISSION IS TO:</h2>
    <p class="mission-body">To evolve the capital projects industry<br>through sharing of knowledge for<br>optimized:</p>
  </div>
  <ul class="pillars">
    <li class="pillar"><svg><use href="#icon-leadership"/></svg><span class="pillar-name">LEADERSHIP</span></li>
    <li class="pillar"><svg><use href="#icon-delivery"/></svg><span class="pillar-name">DELIVERY</span></li>
    <li class="pillar"><svg><use href="#icon-performance"/></svg><span class="pillar-name">PERFORMANCE</span></li>
  </ul>
  <div class="skyline" role="img" aria-label="Photo of glass office towers under construction with cranes against a blue sky"></div>
  <svg class="skyline-edge" viewBox="0 0 304 14" preserveAspectRatio="none"><path d="M0 0h304v2Q152 16 0 2z" fill="#27409b"/></svg>
</section>

<!-- Concept 3 -->
<section class="banner banner--three">
  <svg class="top-band" viewBox="0 0 304 56"><use href="#top-band"/></svg>
  <div class="brand">
    <span class="brand-mark"></span>
    <div class="brand-text">
      <span class="brand-name">C-SoHV</span>
      <span class="brand-rule"></span>
      <span class="brand-full">The Council for Stewardship in Harbor Ventures</span>
    </div>
  </div>
  <div class="hero hero--three" role="img" aria-label="Photo of a construction team reviewing plans at a table with a city skyline and cranes behind"></div>
  <svg class="hero-arch" style="top:160px" viewBox="0 0 304 14" preserveAspectRatio="none"><path d="M0 0h304v12Q152 -4 0 12z" fill="#fff"/></svg>
  <div class="mission">
    <h2 class="mission-title">OUR MISSION IS TO:</h2>
    <p class="mission-body">To evolve the capital projects industry<br>through sharing of knowledge for<br>optimized:</p>
  </div>
  <ul class="pillars">
    <li class="pillar"><svg><use href="#icon-leadership"/></svg><span class="pillar-name">LEADERSHIP</span></li>
    <li class="pillar"><svg><use href="#icon-delivery"/></svg><span class="pillar-name">DELIVERY</span></li>
    <li class="pillar"><svg><use href="#icon-performance"/></svg><span class="pillar-name">PERFORMANCE</span></li>
  </ul>
  <div class="skyline" role="img" aria-label="Photo of glass office towers under construction with cranes against a blue sky"></div>
  <svg class="skyline-edge" viewBox="0 0 304 14" preserveAspectRatio="none"><path d="M0 0h304v2Q152 16 0 2z" fill="#27409b"/></svg>
</section>

<div class="concept-label concept-label--one">1</div>
<div class="concept-label concept-label--two">2</div>
<div class="concept-label concept-label--three">3</div>

</body>
</html>
```